Voltarey - Flyer design

Description -
Motorhome and Caravan EWOFs
Recreational Vehicles (such as caravans, motorhomes, RVs, Boats etc) and Relocatable buildings that can be connected to an electricity supply must be regularly checked for electrical safety. An EWOF needs to be issued every 4 years.
Pre-purchase house inspections
A pre-purchase electrical inspection prior to buying a home can be used to identify any dangerous and unsafe electrical parts of the installation that may be costly to repair once the property has been purchased. Giving you peace of mind when buying your new home.
High risk Electrical inspections
All Prescribed Electrical Work that falls under the High Risk category must be inspected by a Registered Electrical Inspector and have a Record of Inspection certificate issued.
Electric Vehicle Chargers
Any electrical vehicle charger that can be accessed by the public (ie in a non-domestic situation) must be periodically inspected and certified every 12 months.
General Electrical Services
Domestic and commercial - We do new builds, Renovations, Maintenance and more!
Dean Fowler - Electrician and Electrical Inspector
Ph - 0227839152
Dean@voltarey.co.nz
Auckland
------
I also want there to be a few symbols similar to the files I have attached.
The main areas that I am hoping to find work is with caravans/motohomes and EV car chargers so these symbols are quite important.
Thanks so much

```html
<!DOCTYPE html>
<html lang="en">
<head>
<meta charset="utf-8">
<title>Voltarey – Flyer</title>
<link href="https://fonts.googleapis.com/css2?family=Lato:wght@400;700;900&display=swap" rel="stylesheet">
<style>
:root{
  --green:#8cc63f;
  --grey-dark:#666666;
  --grey-text:#5f5f5f;
  --ink:#1f1f1f;
  --white:#ffffff;
  --backdrop:#e4e4e4;
  --overlay:rgba(40,40,40,.72);
}
*{margin:0;padding:0;box-sizing:border-box}
html,body{width:982px;height:1200px;overflow:hidden;background:var(--backdrop);font-family:"Lato",sans-serif}
.flyer{position:absolute;left:66px;top:0;width:1145px;height:1618px;transform:scale(.7417);transform-origin:0 0;background:var(--white);overflow:hidden}
.shapes{position:absolute;inset:0}
.abs{position:absolute;white-space:nowrap}

.brand-name{left:40px;top:66px;font-size:60px;font-weight:700;color:var(--grey-dark);letter-spacing:.5px}

.title-band{position:absolute;left:0;top:275px;width:630px;height:182px;background:var(--overlay)}
.title-name{left:38px;top:282px;font-size:64px;font-weight:700;color:var(--green);letter-spacing:-.5px}
.title-role{left:39px;top:348px;font-size:33px;font-weight:700;color:var(--white)}
.title-role-main{left:37px;top:380px;font-size:58px;font-weight:900;color:var(--white)}

.service{position:absolute;left:102px;width:500px}
.service-head{font-size:29px;font-weight:700;color:var(--grey-text);white-space:nowrap;padding-bottom:8px;border-bottom:2px solid var(--green);width:446px}
.service-head em{font-style:normal;color:var(--green)}
.service-body{margin-top:14px;font-size:21px;line-height:25.5px;color:var(--ink)}
.service-icon{position:absolute;left:25px;width:62px;height:62px}

.panel-title{left:668px;font-size:52px;font-weight:700;color:var(--white)}
.panel-sub{left:668px;font-size:37px;font-weight:700;color:var(--white)}
.panel-body{position:absolute;left:673px;top:848px;font-size:22px;line-height:28px;color:var(--ink)}
.panel-list{position:absolute;left:672px;top:1142px;list-style:none;font-size:27px;font-weight:700;color:var(--ink);line-height:32.5px}
.panel-list li::before{content:"";display:inline-block;width:9px;height:9px;border-radius:50%;background:var(--ink);margin:0 10px 4px 2px}

.call{right:32px;top:1393px;font-size:41px;font-weight:900;color:var(--white)}
.phone{left:742px;top:1475px;font-size:65px;font-weight:700;color:var(--white);letter-spacing:.5px}
.contact-rule{position:absolute;left:672px;top:1560px;width:452px;height:2px;background:var(--green)}
.city{right:35px;top:1568px;font-size:32px;color:var(--white)}
.email{left:87px;top:1550px;font-size:32px;font-weight:700;color:var(--white)}
</style>
</head>
<body>
<div class="flyer">
  <svg class="shapes" viewBox="0 0 1145 1618" width="1145" height="1618">
    <defs>
      <linearGradient id="photoTone" x1="0" y1="0" x2="1" y2="1">
        <stop offset="0" stop-color="#8a8a86"/>
        <stop offset=".45" stop-color="#c9c9c4"/>
        <stop offset=".75" stop-color="#b7c94a"/>
        <stop offset="1" stop-color="#4e5560"/>
      </linearGradient>
    </defs>
    <polygon role="img" aria-label="Photo of an electrician in a hard hat and hi-vis jacket testing a switchboard" fill="url(#photoTone)"
      points="0,196 372,196 620,0 1145,0 1145,560 790,560 568,736 0,736"/>
    <polygon class="accent-stripe" fill="var(--green)" points="585,0 622,0 452,148 436,132"/>
    <polygon class="accent-band" fill="var(--green)" points="0,736 568,736 790,560 1145,560 1145,608 805,608 590,785 0,785"/>
    <polygon class="service-panel" fill="var(--green)" points="808,642 1105,642 1105,1298 770,1298 620,1398 620,790"/>
    <polygon class="footer-accent" fill="var(--green)" points="0,1502 532,1502 672,1412 748,1412 748,1380 1145,1380 1145,1618 0,1618"/>
    <polygon class="footer" fill="var(--grey-dark)" points="0,1530 562,1530 700,1440 785,1440 795,1450 1145,1450 1145,1618 0,1618"/>
    <polygon class="call-tab" fill="var(--green)" points="748,1380 1145,1380 1145,1450 795,1450"/>

    <g class="icon-ev" fill="none" stroke="#111" stroke-width="4" stroke-linejoin="round" stroke-linecap="round">
      <rect x="933" y="665" width="58" height="120" rx="26"/>
      <circle cx="962" cy="695" r="15"/>
      <path d="M965 685 l-7 11 h8 l-7 11"/>
      <path d="M950 730 v30 M960 760 v20"/>
      <path d="M960 760 q30-35 55-20"/>
      <path d="M975 775 v-25 q0-10 10-12 l15-12 h45 l20 22 q15 3 15 15 v12 z"/>
      <path d="M1005 728 v14 h55 M1030 726 v16"/>
      <circle cx="995" cy="775" r="11"/><circle cx="1060" cy="775" r="11"/>
    </g>
    <g class="icon-tools" fill="none" stroke="#111" stroke-width="4" stroke-linecap="round" stroke-linejoin="round">
      <circle cx="1031" cy="1049" r="18"/>
      <path d="M1034 1037 l-8 13 h10 l-8 13"/>
      <path d="M1018 1036 l-25-25 M1044 1036 l25-25 M1018 1062 l-25 25 M1044 1062 l25 25"/>
      <path d="M985 1003 l-8-8 a10 10 0 0 1 14-4 l-6 6 6 6 6-6 a10 10 0 0 1-4 14z"/>
      <path d="M1077 1003 l8-8 a10 10 0 0 0-14-4 l6 6-6 6-6-6 a10 10 0 0 0 4 14z"/>
      <path d="M985 1095 l-8 8 a10 10 0 0 0 14 4 l-6-6 6-6 6 6 a10 10 0 0 0-4-14z"/>
      <path d="M1077 1095 l8 8 a10 10 0 0 1-14 4 l6-6-6-6-6 6 a10 10 0 0 1 4-14z"/>
    </g>
    <circle cx="698" cy="1514" r="29" fill="var(--green)"/>
    <path d="M686 1499 q-4 4 0 14 q8 16 22 20 q8 2 10-3 l-7-7 q-3 2-6 0 q-7-5-10-12 q0-3 2-5 z" fill="var(--white)" opacity=".9"/>
    <g fill="none" stroke="var(--green)" stroke-width="3">
      <rect x="35" y="1556" width="40" height="28"/>
      <path d="M35 1556 l20 16 l20-16 M35 1584 l15-14 M75 1584 l-15-14"/>
    </g>
  </svg>

  <div class="abs brand-name">Voltarey</div>

  <div class="title-band"></div>
  <div class="abs title-name">DEAN FOWLER</div>
  <div class="abs title-role">ELECTRICIAN AND ELECTRICAL</div>
  <div class="abs title-role-main">INSPECTOR</div>

  <svg class="service-icon" style="top:822px" viewBox="0 0 62 62" fill="none" stroke="#555" stroke-width="2.2">
    <rect x="4" y="18" width="50" height="24" rx="4"/><path d="M8 18 q4-10 14-10 h24 q6 0 6 10"/>
    <rect x="9" y="24" width="9" height="7"/><rect x="21" y="24" width="9" height="7"/><path d="M40 24 v18 M48 30 h10 v12 h-4"/>
    <circle cx="16" cy="45" r="5"/><circle cx="44" cy="45" r="5"/>
  </svg>
  <div class="service" style="top:828px">
    <div class="service-head">Motorhome and Caravan <em>EWOFs</em></div>
    <p class="service-body">Recreational Vehicles (such as caravans, motorhomes,<br>RVs, Boats etc) and Relocatable buildings that can be<br>connected to an electricity supply must be regularly<br>checked for electrical safety. An EWOF needs to be<br>issued every 4 years.</p>
  </div>

  <svg class="service-icon" style="top:1028px" viewBox="0 0 62 62" fill="none" stroke="#555" stroke-width="2.2">
    <path d="M4 30 l20-20 l20 20 M8 26 v32 h24"/><rect x="14" y="20" width="18" height="10"/>
    <path d="M14 58 v-12 h8 v12"/><rect x="30" y="30" width="20" height="26"/><path d="M34 38 h12 M34 44 h12 M34 50 h8"/>
    <circle cx="48" cy="50" r="6"/><path d="M52 54 l6 6"/>
  </svg>
  <div class="service" style="top:1038px">
    <div class="service-head">Pre-purchase house <em>inspections</em></div>
    <p class="service-body">A pre-purchase electrical inspection prior to buying<br>a home can be used to identify any dangerous and<br>unsafe electrical parts of the installation that may<br>be costly to repair once the property has been<br>purchased. Giving you peace of mind when buying<br>your new home.</p>
  </div>

  <svg class="service-icon" style="top:1272px" viewBox="0 0 62 62" fill="none" stroke="#555" stroke-width="2.2">
    <path d="M4 30 l20-20 l20 20 M8 26 v32 h24"/><path d="M15 30 l-4 7 h5 l-4 7"/>
    <path d="M18 58 v-12 h8 v12"/><rect x="30" y="30" width="20" height="26"/><path d="M34 38 h12 M34 44 h12 M34 50 h8"/>
    <circle cx="48" cy="50" r="6"/><path d="M52 54 l6 6"/>
  </svg>
  <div class="service" style="top:1283px">
    <div class="service-head">High risk <em>Electrical</em> inspections</div>
    <p class="service-body">All Prescribed Electrical Work that falls under the<br>High Risk category must be inspected by a<br>Registered Electrical Inspector and have a Record<br>of Inspection certificate issued.</p>
  </div>

  <div class="abs panel-title" style="top:746px">Electric</div>
  <div class="abs panel-sub" style="top:802px">Vehicle Chargers</div>
  <p class="panel-body">Any electrical vehicle charger that can<br>be accessed by the public<br>(ie in a non-domestic situation) must be<br>periodically inspected and certified<br>every 12 months.</p>

  <div class="abs panel-title" style="top:1023px">General</div>
  <div class="abs panel-sub" style="top:1080px">Electrical Services</div>
  <ul class="panel-list">
    <li>Domestic and commercial</li>
    <li>We do new builds,</li>
    <li>Renovations,</li>
    <li>Maintenance and more!</li>
  </ul>

  <div class="abs call">CALL US TODAY!</div>
  <div class="abs phone">0227839152</div>
  <div class="contact-rule"></div>
  <div class="abs city">Auckland</div>
  <div class="abs email">Dean@voltarey.co.nz</div>
</div>
</body>
</html>
```